Paul Sefton Personal Card

I am looking for a personal card that has my contact information on the front and then the url for my website on the back. I am a fan of minimal, modern design, but am very open minded to other styles. Both portrait and landscape designs are acceptable. The only other specification that I have is that some sort of graphic of a raven is present somewhere on the card (my last name 'Sefton' means raven in German).
Contact Information for Business Card
Paul Sefton
608.554.1893
paulwsefton@postvane.net
paulwsefton.com
Colors
Designer to choose colors to be used in the design.
Requirements
Must have
- Raven on some part of the card

```html
<!DOCTYPE html>
<html lang="en">
<head>
<meta charset="utf-8">
<title>Paul Sefton Personal Card</title>
<link rel="stylesheet" href="https://fonts.googleapis.com/css2?family=Encode+Sans+Semi+Condensed:wght@400;700&display=swap">
<style>
  :root {
    --backdrop: #e9e7e3;
    --card-white: #ffffff;
    --card-slate: #4f5153;
    --ink: #3a3b3d;
    --ink-strong: #2b2c2e;
    --raven: #1b1b1b;
    --on-slate: #ffffff;
  }
  * { margin: 0; padding: 0; box-sizing: border-box; }
  html, body {
    width: 1200px;
    height: 799px;
    overflow: hidden;
    background: var(--backdrop);
    font-family: "Encode Sans Semi Condensed", "Arial Narrow", sans-serif;
  }
  .canvas {
    position: relative;
    width: 1200px;
    height: 799px;
  }
  .card {
    position: absolute;
    top: 252px;
    width: 520px;
    height: 296px;
    box-shadow: 0 4px 14px rgba(0, 0, 0, 0.12);
  }
  .card--front {
    left: 50px;
    background: var(--card-white);
  }
  .card--back {
    left: 630px;
    background: var(--card-slate);
    display: flex;
    align-items: center;
    justify-content: center;
  }
  .raven-art {
    position: absolute;
    left: 92px;
    top: 100px;
    width: 112px;
    height: 100px;
    border-radius: 46% 54% 40% 60% / 50% 40% 60% 50%;
    background: radial-gradient(ellipse at 45% 45%, var(--raven) 0%, var(--raven) 55%, rgba(27, 27, 27, 0.55) 80%, rgba(27, 27, 27, 0) 100%);
  }
  .contact {
    position: absolute;
    left: 254px;
    top: 127px;
    color: var(--ink);
    line-height: 1.2;
  }
  .contact__name {
    font-weight: 700;
    font-size: 15px;
    letter-spacing: 0.01em;
    text-transform: uppercase;
    color: var(--ink-strong);
  }
  .contact__line {
    font-weight: 400;
    font-size: 14px;
  }
  .website {
    color: var(--on-slate);
    font-weight: 700;
    font-size: 20px;
    letter-spacing: 0.01em;
  }
</style>
</head>
<body>
  <main class="canvas">
    <section class="card card--front" aria-label="Card front">
      <div class="raven-art" role="img" aria-label="Black ink-splatter raven in flight"></div>
      <div class="contact">
        <p class="contact__name">Paul Sefton</p>
        <p class="contact__line">608.554.1893</p>
        <p class="contact__line">paulwsefton@postvane.net</p>
      </div>
    </section>
    <section class="card card--back" aria-label="Card back">
      <p class="website">paulwsefton.com</p>
    </section>
  </main>
</body>
</html>
```